Coralvale Jukebox and Jumping Castle Hire

Hi folks,
This is for a new business based in Brisbane(Australia), the business hires, jukeboxes, inflatable games(mostly jumping castles) and slushy/cocktail machines.
I want the website to appeal to people looking to party. Does that sound too simplistic?
It should be simple to navigate, I require only the front page but make it easy to get to the rest of the site.
Modern, exciting and funky, think rock band or concert promoter.
We are trying to sell packages of products, there should be several packages visible on the front page without looking cluttered.
Link to jukebox song list.
Friendlane, pondlet etc.
I am currently on holidays so I have a fair amount of time to get this project done, it says 10 days I hope to have it done much sooner.

Reason: So far there is no design that I am happy with. I am after a website for Jukeboxes, it should have a rock concert feel.

Ages 20 to 50

Business

• Think rock band type website, black with bold color highlight.
• Plain or bland color.
Pictures of Brisbane or any other city.
Vexaro map or any other location type map.

```html
<!DOCTYPE html>
<html lang="en">
<head>
<meta charset="utf-8">
<title>Coralvale Party Hire</title>
<link href="https://fonts.googleapis.com/css2?family=Lato:ital,wght@0,400;0,700;0,900;1,400&display=swap" rel="stylesheet">
<style>
:root{
  --bg:#050607;
  --panel:#151618;
  --panel-2:#1b1c1f;
  --accent:#3fa9dc;
  --logo:#a9d6f0;
  --label:#3a6ea8;
  --text:#ffffff;
  --muted:#a9acb0;
  --line:#3a3b3e;
  --ctrl:#e8e8e8;
  --pause:#8fd12c;
  --rec:#d11111;
}
*{box-sizing:border-box;margin:0;padding:0}
html,body{width:941px;height:1200px;overflow:hidden;background:var(--bg);font-family:'Lato',sans-serif;color:var(--text)}
.page{position:relative;width:941px;height:1200px;background:radial-gradient(ellipse at 50% 0,#1d2a33 0,var(--bg) 260px)}
.abs{position:absolute}
.site-title{left:0;width:941px;top:24px;text-align:center;font-weight:900;font-size:31px;color:var(--logo);letter-spacing:1px}
.main-nav{left:103px;top:83px;width:733px;height:45px;background:linear-gradient(#3c4650,#20272d);display:flex;align-items:center;justify-content:space-around;font-weight:700;font-size:14px}
.main-nav span{border-right:1px solid rgba(255,255,255,.2);flex:1;text-align:center}
.main-nav span:last-child{border:none}
.main-nav .current{color:var(--logo)}
.hero{left:103px;top:128px;width:735px;height:246px;background:radial-gradient(ellipse at 52% 20%,#6fc6f0 0,#1b5a86 22%,#0c2233 55%,#020406 100%)}
.tagline{left:588px;top:306px;width:250px;height:38px;background:rgba(16,40,56,.9);clip-path:polygon(6% 0,100% 0,100% 100%,0 100%);color:#c8e4f4;font-size:21px;font-weight:700;line-height:38px;text-align:right;padding-right:4px}
.player{left:103px;top:376px;width:734px;height:40px;border-radius:20px;background:linear-gradient(#3a3c40,#111214);border:1px solid #555}
.player .btn{position:absolute;top:7px;width:25px;height:25px;border-radius:50%;background:linear-gradient(#4a4c50,#0e0f10);border:1px solid #666}
.player .btn svg{display:block;width:23px;height:23px}
.player .screen{position:absolute;left:192px;top:10px;width:195px;height:20px;border-radius:10px;background:#050505;border:1px solid #555;font-size:7px;line-height:18px}
.categories{left:103px;top:416px;width:735px;height:178px;background:var(--panel)}
.tile{position:absolute;top:12px;width:165px;height:148px}
.tile .photo{height:122px}
.tile .label{height:26px;background:var(--label);text-align:center;font-weight:700;font-size:14px;line-height:26px}
h2{font-size:20px;font-weight:700}
h2 em{font-style:normal;color:var(--accent)}
.about{left:102px;top:612px;width:232px}
.about h3{font-size:12px;font-weight:700;margin:14px 0 8px}
.about p,.event p{font-size:10.4px;line-height:13.4px;color:var(--muted)}
.video{left:356px;top:612px}
.video .frame{margin-top:13px;width:226px;height:102px;border:1px solid #555;padding:3px;background:#111}
.video .still{width:100%;height:100%;background:linear-gradient(120deg,#3b2540,#a33a3a 40%,#d9a26a 60%,#233a66)}
.events{left:610px;top:612px;width:214px}
.event{display:flex;gap:6px;padding:10px 0 8px;border-bottom:1px solid var(--line)}
.event:last-child{border:none}
.date{flex:none;width:38px;height:38px;border-radius:50%;background:#2c2e31;text-align:center;color:var(--accent);font-size:17px;line-height:17px;padding-top:4px}
.date small{display:block;font-size:10px;color:#888}
.reviews{left:103px;top:780px;width:735px;height:184px;background:var(--panel-2);text-align:center}
.reviews h2{margin-top:12px}
.avatar{width:54px;height:54px;border-radius:50%;margin:9px auto 0;background:radial-gradient(circle,#c79a7a,#3b3d40);border:2px solid #666}
.quote{font-style:italic;font-size:15px;margin-top:11px;color:#ddd}
.quote b{font-style:normal;font-size:26px;color:#666;vertical-align:-8px;font-weight:900}
.review-body{font-style:italic;font-size:10px;line-height:15px;color:var(--muted);margin:6px 40px 0}
.arrow{position:absolute;top:81px;width:22px;height:22px}
.rule{left:103px;top:994px;width:736px;height:1px;background:var(--line)}
.map{left:104px;top:1022px;width:214px;height:122px;background:linear-gradient(135deg,#e2e3e4,#b9bbbd);border:2px solid #888}
.contact{left:338px;top:1020px;width:180px;font-size:10px;color:#ddd}
.contact .row{display:flex;gap:10px;align-items:flex-start;margin-bottom:10px}
.contact .row svg{flex:none}
.contact .big{font-size:12px;color:#fff}
.newsletter{left:537px;top:1020px;width:150px}
.newsletter h4{font-size:13px;font-weight:400;margin-bottom:10px}
.newsletter .field{width:147px;height:22px;background:#fff;color:#999;font-style:italic;font-size:8px;padding:6px}
.newsletter .submit{margin-top:8px;width:66px;height:22px;background:var(--label);font-weight:700;font-size:12px;text-align:center;line-height:22px}
.newsletter p{margin-top:15px;font-size:8px;line-height:10px}
.footer-logo{left:706px;top:1036px;width:136px;text-align:center;font-weight:900;font-size:20px;line-height:26px;color:#b9bcc0}
.social{left:708px;top:1122px;width:130px;display:flex;justify-content:space-between;font-size:8px;font-weight:700}
.social span{display:flex;align-items:center;gap:3px;white-space:nowrap}
.social i{width:6px;height:6px;border-radius:50%;background:#fff}
.bottom-bar{left:103px;top:1164px;width:736px;height:36px;background:linear-gradient(#2a2c2f,#141517);text-align:center;font-size:11px;font-weight:700;line-height:36px}
</style>
</head>
<body>
<div class="page">
  <div class="abs site-title">Coralvale Party Hire</div>

  <nav class="abs main-nav">
    <span class="current">HOME</span><span>ABOUT US</span><span>AUDIO</span><span>GALLERY</span><span>NEWS</span><span>PACKAGES</span><span>CONTACT</span>
  </nav>

  <div class="abs hero" role="img" aria-label="Concert crowd under blue stage lights"></div>
  <div class="abs tagline">Live Today,&nbsp; Paty Now.</div>

  <div class="abs player">
    <span class="btn" style="left:9px" aria-label="Previous"><svg viewBox="0 0 23 23"><rect x="6" y="7" width="2" height="9" fill="var(--ctrl)"/><path d="M16 7v9l-7-4.5z" fill="var(--ctrl)"/></svg></span>
    <span class="btn" style="left:39px" aria-label="Play"><svg viewBox="0 0 23 23"><path d="M9 6.5v10l8-5z" fill="var(--ctrl)"/></svg></span>
    <span class="btn" style="left:69px" aria-label="Pause"><svg viewBox="0 0 23 23"><rect x="7.5" y="6.5" width="3" height="10" fill="var(--pause)"/><rect x="12.5" y="6.5" width="3" height="10" fill="var(--pause)"/></svg></span>
    <span class="btn" style="left:99px" aria-label="Next"><svg viewBox="0 0 23 23"><path d="M7 7v9l7-4.5z" fill="var(--ctrl)"/><rect x="15" y="7" width="2" height="9" fill="var(--ctrl)"/></svg></span>
    <span class="btn" style="left:129px" aria-label="Record"><svg viewBox="0 0 23 23"><circle cx="11.5" cy="11.5" r="5.5" fill="var(--rec)"/></svg></span>
    <div class="screen">
      <span style="position:absolute;left:0;width:40px;height:18px;background:#ccc;color:#000;border-radius:9px 0 0 9px;text-align:center;font-weight:700">playing</span>
      <span style="position:absolute;left:46px;color:#9f3">Funky Track</span>
      <span style="position:absolute;left:116px;top:3px;width:26px;height:11px;background:linear-gradient(90deg,#fc3,#f60)"></span>
      <span style="position:absolute;left:158px;color:#9f3">0.52:25</span>
    </div>
    <svg style="position:absolute;left:435px;top:14px" width="290" height="12">
      <rect x="0" y="4" width="176" height="4" rx="2" fill="#777"/>
      <rect x="0" y="4" width="66" height="4" rx="2" fill="#7c3"/>
      <circle cx="66" cy="6" r="4" fill="#ddd"/>
      <path d="M190 4h3l4-3v10l-4-3h-3z" fill="#bbb"/>
      <rect x="206" y="4" width="66" height="4" rx="2" fill="#777"/>
      <rect x="206" y="4" width="42" height="4" rx="2" fill="#d11"/>
      <circle cx="248" cy="6" r="4" fill="#ddd"/>
      <path d="M280 4h8l-4 5z" fill="#777"/>
    </svg>
  </div>

  <section class="abs categories">
    <div class="tile" style="left:14px"><div class="photo" role="img" aria-label="Lit jukebox" style="background:linear-gradient(90deg,#4a2a10,#d98a2a,#2a2a6a)"></div><div class="label">JUKEBOXES</div></div>
    <div class="tile" style="left:194px"><div class="photo" role="img" aria-label="Inside a jumping castle" style="background:linear-gradient(#b01010,#e02020,#401020)"></div><div class="label">JUMPING CASTLES</div></div>
    <div class="tile" style="left:374px"><div class="photo" role="img" aria-label="Slushy machine with coloured drinks" style="background:linear-gradient(90deg,#1a6ad0,#2aa0f0,#d03050,#e0d030)"></div><div class="label">SLUSHY MACHINE</div></div>
    <div class="tile" style="left:555px"><div class="photo" role="img" aria-label="Cocktails in glasses" style="background:linear-gradient(#c04a1a,#d08a2a,#c0c020)"></div><div class="label">COCKTAIL MACHINES</div></div>
  </section>

  <section class="abs about">
    <h2><em>Shortly</em> About us</h2>
    <h3>Fusce scelerisque nulla sit amets dignissim</h3>
    <p>Lorem ipsum dolor sit amet, consectetu adipiscing elit. Maecenas at justo nec orci vestibulum luctus ac quis augue. Phasellus at consequat est. Aliquam posuere euismod viverra. Donec ultrices qua vitae mauris ullamcorper, nec bla Maecenas malesuada lacinia luctus. Pellentesque.</p>
  </section>

  <section class="abs video">
    <h2><em>Watch</em> Video</h2>
    <div class="frame">
      <div class="still" role="img" aria-label="Friends celebrating at a party, video still">
        <svg width="218" height="94"><circle cx="109" cy="47" r="17" fill="none" stroke="#fff" stroke-width="3"/><path d="M103 38l14 9-14 9z" fill="#fff"/></svg>
      </div>
    </div>
  </section>

  <section class="abs events">
    <h2><em>Upcoming</em>&nbsp; Events</h2>
    <div class="event"><div class="date">19<small>oct</small></div><p>Lorem ipsum dolor sit am consectetu adipiscing elit. Maecenas at justo nec orci vestibulum luctus ac quis.</p></div>
    <div class="event"><div class="date">19<small>oct</small></div><p>Lorem ipsum dolor sit am consectetu adipiscing elit. Maecenas at justo nec orci vestibulum luctus ac quis.</p></div>
  </section>

  <section class="abs reviews">
    <h2><em>Customers</em> Review</h2>
    <div class="avatar" role="img" aria-label="Customer portrait"></div>
    <p class="quote"><b>&#8220;</b> Vestibulum porta, diam quis auctor ultricies, dui quam dapibus ligula, consectetur <b>&#8221;</b></p>
    <p class="review-body">Lorem ipsum dolor sit amet, consectetur adipiscing elit. Integer venenatis tincidunt elit, aliquam semper quam pulvinar id. Aliquam erat volutpat. Integer nulla urna, sagittis sed viverra quis, tincidunt vel felis. Pellentesque eleifend sem ut diam bibendum, non sagittis sapien pellentesque. Etiam semper</p>
    <svg class="arrow" style="left:15px" viewBox="0 0 22 22"><circle cx="11" cy="11" r="10" fill="none" stroke="#888"/><path d="M13 6l-5 5 5 5" fill="none" stroke="#888" stroke-width="1.5"/></svg>
    <svg class="arrow" style="right:15px" viewBox="0 0 22 22"><circle cx="11" cy="11" r="10" fill="none" stroke="#888"/><path d="M9 6l5 5-5 5" fill="none" stroke="#888" stroke-width="1.5"/></svg>
  </section>

  <div class="abs rule"></div>

  <div class="abs map" role="img" aria-label="Street map of the business location"></div>

  <div class="abs contact">
    <div class="row">
      <svg width="24" height="24"><circle cx="12" cy="12" r="11" fill="none" stroke="#fff" stroke-width="1.5"/><path d="M12 5v7h5" fill="none" stroke="#fff" stroke-width="1.5"/></svg>
      <div><div class="big">Open everyday</div>from 12a.m. to 2:15p.m.<br>and 6p.m. to midnight</div>
    </div>
    <div class="row">
      <svg width="24" height="18"><path d="M12 1a5 5 0 0 1 5 5c0 4-5 10-5 10S7 10 7 6a5 5 0 0 1 5-5z" fill="#fff"/><circle cx="12" cy="6" r="2" fill="#050607"/></svg>
      <div class="big" style="font-size:10.5px">Lorem ipsum dolor sit ametin<br>Coralvale, QLD 4170</div>
    </div>
    <div class="row">
      <svg width="24" height="16"><path d="M6 2l3 0 1 4-2 1c1 2 2 3 4 4l1-2 4 1v3c-7 1-12-5-11-11z" fill="#fff"/></svg>
      <div class="big" style="font-size:10.5px">123 4567890</div>
    </div>
    <div class="row">
      <svg width="24" height="14"><rect x="4" y="2" width="16" height="11" fill="none" stroke="#fff" stroke-width="1.3"/><path d="M4 2l8 6 8-6M4 13l6-5M20 13l-6-5" fill="none" stroke="#fff" stroke-width="1.3"/></svg>
      <div class="big" style="font-size:10.5px">info@coralvaleparty.com</div>
    </div>
  </div>

  <div class="abs newsletter">
    <h4>Stay in Touch</h4>
    <div class="field">Enter your email.....</div>
    <div class="submit">SUBMIT</div>
    <p>We never Share your email address with another third party.</p>
  </div>

  <div class="abs footer-logo">Coralvale<br>Party Hire</div>

  <div class="abs social">
    <span><i></i>Friendlane</span><span><i></i>pondlet</span><span><i></i>Linkora</span>
  </div>

  <div class="abs bottom-bar">© 2014, Coralvale Party Hire&nbsp; All Rights Reserved</div>
</div>
</body>
</html>
```